Tasman Curdworks Guild needs new business cards

We need new business cards designed and produced. We are likely to need other design work done for ads, flyers etc in future.

We would like to start with an initial business card.

The Tasman Curdworks Guild (TCG) is a membership-based not-for-profit organisation that looks after the interests of Australia's small to medium artisan cheesemakers, many of whom are also small-scale farmers. The design should be simple, using our logo, but also communicate our artisan cheese and small dairy farm focus.

The first card to be designed and produced is for me, Miriam Tolhurst. My details are:

Miriam Tolhurst
Secretary
Tasman Curdworks Guild (TCG)
http://www.curdworksguild.example
T +61452837190
E miriam.miriamtolhurst@mailbox.example

I have attached the TCG logo in jpg form. I have a higher resolution version available if needed.

Thank you!

Miriam

Miriam Tolhurst
Tasman Curdworks Guild
miriam.miriamtolhurst@mailbox.example
+61452837190

Sans Serif

• Logo (see attached file)

```html
<!DOCTYPE html>
<html lang="en">
<head>
<meta charset="utf-8">
<title>Tasman Curdworks Guild – Business Card</title>
<link href="https://fonts.googleapis.com/css2?family=Open+Sans:wght@400;600&display=swap" rel="stylesheet">
<style>
  :root {
    --backdrop: #cfcfd3;
    --card: #ffffff;
    --brown: #5a3e22;
    --ink: #4a4a4a;
    --gold: #efc65c;
  }
  html, body {
    margin: 0;
    width: 1200px;
    height: 1200px;
    overflow: hidden;
    background: var(--backdrop);
    font-family: "Open Sans", Arial, sans-serif;
  }
  .card {
    position: absolute;
    left: 180px;
    width: 840px;
    height: 480px;
    background: var(--card);
    box-shadow: 0 6px 18px rgba(0,0,0,0.18);
    box-sizing: border-box;
  }
  .card--front { top: 90px; }
  .card--back { top: 630px; }

  .brand {
    display: flex;
    align-items: center;
    gap: 18px;
    color: var(--brown);
    font-weight: 400;
  }
  .brand__dot {
    border-radius: 50%;
    background: var(--gold);
    flex: none;
  }
  .card--front .brand {
    position: absolute;
    left: 50%;
    top: 50%;
    transform: translate(-50%, -50%);
    font-size: 38px;
  }
  .card--front .brand__dot { width: 64px; height: 64px; }

  .card--back .brand {
    position: absolute;
    left: 60px;
    top: 70px;
    font-size: 24px;
    gap: 12px;
  }
  .card--back .brand__dot { width: 40px; height: 40px; }

  .contact {
    position: absolute;
    right: 60px;
    top: 66px;
    font-size: 17px;
    line-height: 1.5;
    color: var(--ink);
  }
  .contact__label { color: var(--brown); font-weight: 600; }

  .website {
    position: absolute;
    right: 60px;
    top: 230px;
    font-size: 17px;
    color: var(--ink);
  }

  .person {
    position: absolute;
    left: 60px;
    bottom: 60px;
  }
  .person__name {
    margin: 0;
    font-size: 32px;
    font-weight: 600;
    color: var(--brown);
    line-height: 1.1;
  }
  .person__role {
    margin: 2px 0 0 4px;
    font-size: 19px;
    color: var(--ink);
  }
</style>
</head>
<body>
  <section class="card card--front">
    <div class="brand">
      <span class="brand__dot"></span>
      <span class="brand__name">Tasman Curdworks Guild</span>
    </div>
  </section>

  <section class="card card--back">
    <div class="brand">
      <span class="brand__dot"></span>
      <span class="brand__name">Tasman Curdworks Guild</span>
    </div>

    <div class="contact">
      <div><span class="contact__label">T:</span> +61452837190</div>
      <div><span class="contact__label">E:</span> miriamtolhurst@mailbox.example</div>
    </div>

    <div class="website">www.curdworksguild.example</div>

    <div class="person">
      <p class="person__name">Miriam Tolhurst</p>
      <p class="person__role">Secretary</p>
    </div>
  </section>
</body>
</html>
```